Refresh of Business Card Design

Want to refresh the business card design with the new logo while adhering to style guide as attached. Would like to match feel of website www.durmackvinex.com

```html
<!DOCTYPE html>
<html lang="en">
<head>
<meta charset="utf-8">
<title>Durmack Vinex Business Card</title>
<link rel="stylesheet" href="https://fonts.googleapis.com/css2?family=Work+Sans:wght@400;500;700&display=swap">
<style>
  :root {
    --page-bg: #eeeeee;
    --card-bg: #04080a;
    --accent: #e8214a;
    --text-light: #ffffff;
    --text-muted: #e6e6e6;
    --brand-circle: #c9202b;
  }
  * { margin: 0; padding: 0; box-sizing: border-box; }
  html, body {
    width: 1200px; height: 979px; overflow: hidden;
    background: var(--page-bg);
    font-family: "Work Sans", Arial, sans-serif;
  }
  .card {
    position: absolute; left: 299px; top: 260px;
    width: 668px; height: 382px;
    background: var(--card-bg);
    color: var(--text-light);
  }
  .brand {
    position: absolute; left: 18px; top: 110px; width: 240px;
    display: flex; flex-direction: column; align-items: center; gap: 14px;
  }
  .brand-mark {
    width: 64px; height: 64px; border-radius: 50%;
    background: var(--brand-circle);
  }
  .brand-name {
    font-size: 21px; font-weight: 500; letter-spacing: 1px;
    color: var(--text-light); white-space: nowrap;
  }
  .name-band {
    position: absolute; left: 298px; top: 25px;
    width: 372px; height: 81px;
    background: var(--accent);
    border-radius: 10px 0 0 10px;
    padding: 6px 0 0 32px;
  }
  .person-name {
    font-size: 34px; font-weight: 700; line-height: 40px; letter-spacing: 0.3px;
    white-space: nowrap;
  }
  .person-role {
    font-size: 23px; font-weight: 400; line-height: 28px; padding-left: 4px; letter-spacing: 0.5px;
    white-space: nowrap;
  }
  .contact-list { position: absolute; left: 318px; top: 0; list-style: none; }
  .contact-item {
    position: absolute; left: 0; display: flex; align-items: flex-start;
    font-size: 16px; line-height: 21px; color: var(--text-muted);
    white-space: nowrap; letter-spacing: 0.2px;
  }
  .contact-item svg { width: 32px; flex: none; }
  .contact-text { padding-left: 12px; }
  .contact-phone { top: 148px; }
  .contact-email { top: 196px; }
  .contact-email .contact-text { margin-top: -1px; }
  .contact-address { top: 236px; }
  .website {
    position: absolute; left: 0; right: 0; top: 340px;
    text-align: center; font-size: 20px; letter-spacing: 0.5px; white-space: nowrap;
  }
</style>
</head>
<body>
  <article class="card">
    <div class="brand">
      <div class="brand-mark"></div>
      <div class="brand-name">DURMACK VINEX</div>
    </div>

    <header class="name-band">
      <h1 class="person-name">ROWAN PETRELLI</h1>
      <p class="person-role">SALES</p>
    </header>

    <ul class="contact-list">
      <li class="contact-item contact-phone">
        <svg viewBox="0 0 32 32" height="32" fill="none" stroke="var(--accent)" stroke-width="1.6" stroke-linejoin="round">
          <path d="M6 4 L11 3 L14 10 L11 12 C12.5 16 15.5 19.5 20 21 L22 18 L29 21 L28 26 C27 28 24 29 21 28 C13 25 7 19 4 11 C3 8 4 5 6 4 Z"/>
        </svg>
        <span class="contact-text">+555 - 201 - 3948</span>
      </li>
      <li class="contact-item contact-email">
        <svg viewBox="0 0 32 22" height="22" fill="none" stroke="var(--accent)" stroke-width="1.6" stroke-linejoin="round">
          <rect x="1" y="2" width="30" height="18"/>
          <path d="M1 2 L16 13 L31 2 M1 20 L12 10 M31 20 L20 10"/>
        </svg>
        <span class="contact-text">rpetrelli@durmackvinex.com</span>
      </li>
      <li class="contact-item contact-address">
        <svg viewBox="0 0 32 36" height="36" fill="none" stroke="var(--accent)" stroke-width="1.6">
          <path d="M16 34 C9 25 4 19 4 13 A12 12 0 0 1 28 13 C28 19 23 25 16 34 Z"/>
          <circle cx="16" cy="13" r="5"/>
        </svg>
        <span class="contact-text">P.O. Box 40213 Harwell, TX 70455<br>72 Ridge Ln Calloway, Texas 70418</span>
      </li>
    </ul>

    <p class="website">www.durmackvinex.com</p>
  </article>
</body>
</html>
```